Web Redesign

Hi,
We have a created a webpage on pagemill using a theme called Quorvel which can be downloaded at Skin Pantry which we like the look and feel of.

You can view our current page we are building at:: www.tillbrookhelp.com.au

The text needs altering which we will do ourselves. Basically, we are requiring the graphic elements that should be placed on EACh page.

The webpage we like the look and feel of is:
http://www.moonlark.com.au/
http://www.codevix.com.au/

Ideas for pages:
Our process - could be something along the lines of http://www.codevix.com.au/our-method
Our service - could be something along the lines of http://www.moonlark.com.au/iphone-application-development/
Our work - could be something along the lines of http://www.codevix.com.au/our-work
Our Value Proposition - could be something along hte lines of http://www.moonlark.com.au/services/
About Us - happy to go with your suggestion
Contact us - happy to use what we have currently if you can come up with a suitable graphic http://tillbrookhelp.com.au/contact-example-1/
FAQ - happy to use what we have currently if you can come up with a suitable graphic http://tillbrookhelp.com.au/contact-example-1/

We would like you to come up with the design/graphics and add then once the winner of the project is chosen we could give you the admin login details to upload the images or we could do it ourselves if you supplied them all and in which case would be good to know where you envision they would be placed.

To give you some insight, this is a branch from business we have called HandBolt (www.handbolt.org) where we aggregate charities onto the one platform for smart phones and allow people to donate to their favourite charity anywhere, anytime with the push of a button.
Tillbrookhelp is a side business to this where we have began building white labelled Tillbrookhelp on our HandBolt platform and we wanted a separate webpage for this.

Once this webpage is completed, we would love to get the HandBolt webpage revamped so there is further opportunity to work with you on this project.

Happy to answer any questions if needed.

Thanks and look forward to seeing the designs

Our Ideas for pages:

Target Market(s)

Charities, corporates

Industry/Entity Type

Building

```html
<!DOCTYPE html>
<html lang="en">
<head>
<meta charset="utf-8">
<title>Tillbrookhelp — Home</title>
<link rel="stylesheet" href="https://fonts.googleapis.com/css2?family=Source+Sans+3:ital,wght@0,400;0,600;0,700;1,400&family=Arimo:wght@400;700&family=Questrial&display=swap">
<style>
:root{
  --ink:#333;
  --muted:#555;
  --blue-text:#1a6fa0;
  --hero-deep:#0e5a86;
  --sky-1:#bfeefb;
  --sky-2:#5cd0f0;
  --orange:#f7941d;
  --nav-dark:#2e2e2e;
  --footer:#2b2b2b;
  --footer-base:#1e1e1e;
  --footer-text:#d8d8d8;
  --footer-head:#9a9a9a;
  --card-line:#e2e2e2;
}
*{box-sizing:border-box;margin:0;padding:0}
html,body{width:848px;height:1200px;overflow:hidden;background:#fff}
body{position:relative;font-family:"Source Sans 3",sans-serif;color:var(--ink)}
.abs{position:absolute}

/* navigation */
.site-nav{left:0;top:0;width:848px;height:38px;background:linear-gradient(#fff,#f2f2f2);border-bottom:3px solid #333}
.site-nav ul{list-style:none;position:absolute;left:65px;top:0;display:flex;height:36px;border-left:1px solid #ddd}
.site-nav li{font-family:"Arimo",sans-serif;font-size:12px;font-weight:700;color:#666;padding:0 14px;line-height:40px;border-right:1px solid #ddd}
.site-nav li.active{background:linear-gradient(#555,#2a2a2a);color:#fff;padding:0 18px}

/* hero */
.hero{left:0;top:40px;width:848px;height:372px;background:radial-gradient(ellipse at 25% 55%,#eafaff 0%,var(--sky-1) 35%,var(--sky-2) 100%);border-bottom:1px solid #3aa9cc}
.brand-bar{left:63px;top:47px;width:722px;height:67px;background:#fff;border-radius:2px;box-shadow:0 3px 6px rgba(0,0,0,.18)}
.brand-name{left:8px;top:10px;font-family:"Questrial",sans-serif;font-size:32px;color:#333;letter-spacing:-.5px}
.social-sq{top:25px;width:16px;height:16px;border-radius:3px}
.search{left:595px;top:23px;width:120px;height:20px;border:1px solid #ccc;background:linear-gradient(#fafafa,#eee);font-size:9px;color:#444;padding:4px 9px}
.search svg{position:absolute;right:6px;top:4px}
.hero-kicker{left:63px;top:160px;font-size:27px;color:var(--hero-deep);font-weight:400;letter-spacing:-.3px}
.hero-title{left:63px;top:187px;font-size:31px;font-weight:700;color:var(--hero-deep);letter-spacing:-.3px}
.hero-copy{left:65px;top:224px;width:290px;font-size:10.5px;line-height:14.5px;color:var(--blue-text)}
.cta-orange{left:66px;top:278px;width:119px;height:30px;background:linear-gradient(#ffa630,#f08010);color:#fff;font-weight:700;font-size:12px;text-align:center;line-height:30px}
.dots{left:65px;top:339px;display:flex;gap:3px}
.dots i{width:9px;height:9px;border-radius:50%;background:#9ad2e8}
.dots i.on{background:#1866a0}
.device{border-radius:16px;background:linear-gradient(160deg,#3a3a3a,#0d0d0d)}

/* features */
.feature{width:171px}
.feature .shot{height:101px;border:4px solid #fff;box-shadow:0 1px 3px rgba(0,0,0,.2)}
.feature p{margin-top:14px;font-family:"Arimo",sans-serif;font-weight:700;font-size:11.5px;line-height:16px;color:#555;text-align:center}
.rule{left:63px;top:609px;width:722px;height:1px;background:var(--card-line)}
.intro{left:70px;top:627px;width:528px;font-family:"Arimo",sans-serif;font-size:12.5px;line-height:19px;color:var(--blue-text);text-align:justify}
.btn-dark{left:70px;top:697px;width:151px;height:33px;background:linear-gradient(#555,#1f1f1f);border-radius:3px;color:#fff;font-family:"Arimo",sans-serif;font-size:11px;font-weight:700;line-height:33px;padding-left:31px}
.btn-dark i{position:absolute;left:12px;top:10px;width:13px;height:13px;border-radius:50%;background:#111}
.press{left:611px;top:631px;width:173px;height:98px;border:1px solid #ddd;padding:3px}
.press-inner{width:100%;height:100%;background:#efefef;text-align:center;padding-top:24px}
.press-name{font-family:"Source Sans 3",sans-serif;font-weight:700;font-size:15px;color:#222;line-height:16px}

/* testimonials */
.section-title{left:70px;top:793px;font-size:20px;color:#333}
.testimonial{width:236px}
.quote-open{left:0;top:0;font-family:Georgia,serif;font-size:32px;color:#bbb;line-height:28px}
.avatar{left:21px;top:2px;width:61px;height:56px;border:2px solid #fff;box-shadow:0 0 2px rgba(0,0,0,.35)}
.t-lead{left:93px;top:0;width:140px;font-style:italic;font-size:9px;line-height:15px;color:#444}
.t-body{left:19px;top:64px;width:217px;font-style:italic;font-size:9px;line-height:15px;color:#444}
.t-author{left:20px;top:116px;font-size:9px;font-weight:600;color:#444}

/* footer */
.footer{left:0;top:978px;width:848px;height:178px;background:var(--footer)}
.footer-base{left:0;top:1156px;width:848px;height:44px;background:var(--footer-base)}
.f-col h4{font-weight:400;font-size:15px;color:var(--footer-head);margin-bottom:10px}
.f-col li{list-style:none;font-size:9.5px;color:var(--footer-text);line-height:21px}
.f-divider{top:1000px;width:1px;height:144px;background:#444}
.tweet{font-size:9.5px;color:var(--footer-text);line-height:16px;width:210px}
.tweet small{display:block;color:#aaa;font-size:9px;margin-top:5px}
.connect li{display:flex;align-items:center;gap:11px;height:27px;font-style:italic;font-size:9.5px}
.connect i{width:22px;height:22px;border-radius:50%;background:#fff}
.copyright{left:65px;top:1172px;font-size:9px;color:#999}
</style>
</head>
<body>

<nav class="site-nav abs">
  <ul>
    <li class="active">Home</li><li>Our Process</li><li>Our Services</li><li>Our Work</li><li>Our Value Proposition</li><li>About us</li><li>Contact Us</li><li>FAQ</li>
  </ul>
</nav>

<section class="hero abs"></section>

<header class="brand-bar abs">
  <div class="brand-name abs">Tillbrookhelp</div>
  <span class="social-sq abs" style="left:547px;background:#3b5a9a"></span>
  <span class="social-sq abs" style="left:569px;background:#3cc4ee"></span>
  <div class="search abs">Search
    <svg width="12" height="12" viewBox="0 0 12 12"><circle cx="4.5" cy="4.5" r="3.3" fill="none" stroke="#222" stroke-width="1.8"/><path d="M7 7l4 4" stroke="#222" stroke-width="2.2" stroke-linecap="round"/></svg>
  </div>
</header>

<div class="hero-kicker abs">THE FUTURE OF</div>
<h1 class="hero-title abs">GIVING IS MOBILE APP</h1>
<p class="hero-copy abs">Mauris vel lacus vitae felis vestibulum volutpat. Etiam est nunc, venenatis in, tristique eu, imperdiet ac, nisl. Cum sociis natoque penatibus et magnis dis parturient montes</p>
<div class="cta-orange abs">HELP ME GO MOBILE</div>
<div class="dots abs"><i class="on"></i><i></i><i></i><i></i></div>

<div class="device abs" style="left:608px;top:192px;width:82px;height:202px" role="img" aria-label="Second smartphone showing the charity app home screen"></div>
<div class="device abs" style="left:482px;top:138px;width:134px;height:260px" role="img" aria-label="Smartphone showing the donation screen with sponsor amounts and a Donate Now button"></div>

<div class="feature abs" style="left:63px;top:430px">
  <div class="shot" style="background:linear-gradient(135deg,#6b4a3a,#1d1d1d)" role="img" aria-label="Hand holding a smartphone"></div>
  <p>The App Branded with your organisation's Name and Logo</p>
</div>
<div class="feature abs" style="left:247px;top:430px">
  <div class="shot" style="background:linear-gradient(135deg,#d9c8b0,#8a6e55)" role="img" aria-label="Person paying by card on a phone"></div>
  <p>Receive Donations Immedi-ately - safe and secure PCI compiant donation platform</p>
</div>
<div class="feature abs" style="left:431px;top:430px">
  <div class="shot" style="background:linear-gradient(135deg,#4a4a4a,#111)" role="img" aria-label="Hands typing on a tablet"></div>
  <p>Your control the contents - It's real easy to update!</p>
</div>
<div class="feature abs" style="left:614px;top:430px">
  <div class="shot" style="background:linear-gradient(135deg,#c9c9c9,#6d5a55)" role="img" aria-label="Group of people shouting through megaphones"></div>
  <p>Mount a campaign in seconds - See the funds flow in!</p>
</div>

<div class="rule abs"></div>
<p class="intro abs">Connect and engage your donor base through a custom App, branded with your logo. Enhance your donations through the completely integrated donation platform, including personalised receipts and dashboard reporting.</p>
<div class="btn-dark abs"><i></i>PURCHASE APP</div>

<aside class="press abs">
  <div class="press-inner">
    <div class="press-name">THE COASTLINE<br>POST</div>
    <svg width="24" height="10" viewBox="0 0 24 10" style="margin-top:14px"><path d="M7 1L1 5l6 4z" fill="#111"/><path d="M17 1l6 4-6 4z" fill="#111"/></svg>
  </div>
</aside>

<h2 class="section-title abs" style="font-weight:400">Customer Testimonials</h2>

<div class="testimonial abs" style="left:64px;top:834px;height:130px">
  <div class="quote-open abs">&ldquo;</div>
  <div class="avatar abs" style="background:#b98e74" role="img" aria-label="Portrait of a customer"></div>
  <p class="t-lead abs">Nunc tempus felis vitae urna. Vivamus porttitor, neque at volut-pat rutrum, purus nisi eleifend libero, a tempus libero lectus</p>
  <p class="t-body abs">Morbi eget arcu. Morbi porta, libero id ullamcorper non-ummy, nibh ligula pulvinar metus, eget consectetuer augue nisi quis lacus. Ut ac mi quis lacus. <span style="font-family:Georgia,serif;font-size:16px;color:#bbb;font-style:normal">&rdquo;</span></p>
  <div class="t-author abs">By Author Name</div>
</div>
<div class="testimonial abs" style="left:311px;top:834px;height:130px">
  <div class="quote-open abs">&ldquo;</div>
  <div class="avatar abs" style="background:#a7876a" role="img" aria-label="Portrait of a customer"></div>
  <p class="t-lead abs">Nunc tempus felis vitae urna. Vivamus porttitor, neque at volut-pat rutrum, purus nisi eleifend libero, a tempus libero lectus</p>
  <p class="t-body abs">Morbi eget arcu. Morbi porta, libero id ullamcorper non-ummy, nibh ligula pulvinar metus, eget consectetuer augue nisi quis lacus. Ut ac mi quis lacus. <span style="font-family:Georgia,serif;font-size:16px;color:#bbb;font-style:normal">&rdquo;</span></p>
  <div class="t-author abs">By Author Name</div>
</div>
<div class="testimonial abs" style="left:558px;top:830px;height:130px">
  <div class="quote-open abs">&ldquo;</div>
  <div class="avatar abs" style="background:#9f7a63" role="img" aria-label="Portrait of a customer"></div>
  <p class="t-lead abs">Nunc tempus felis vitae urna. Vivamus porttitor, neque at volut-pat rutrum, purus nisi eleifend libero, a tempus libero lectus</p>
  <p class="t-body abs">Morbi eget arcu. Morbi porta, libero id ullamcorper non-ummy, nibh ligula pulvinar metus, eget consectetuer augue nisi quis lacus. Ut ac mi quis lacus. <span style="font-family:Georgia,serif;font-size:16px;color:#bbb;font-style:normal">&rdquo;</span></p>
  <div class="t-author abs">By Author Name</div>
</div>

<footer class="footer abs"></footer>
<div class="f-col abs" style="left:102px;top:997px">
  <h4>COMPANY</h4>
  <ul><li>COMPANY OVERVIEW</li><li>ABOUT US</li><li>SERVICES PROVIDE</li><li>OUR PROCESS</li><li>OUR CLIENTS</li></ul>
</div>
<div class="f-col abs" style="left:233px;top:997px">
  <h4>WHAT WE DO</h4>
  <ul><li>VALUE PROPOSITION</li><li>OUR WORK</li><li>TESTIMONIALS</li><li>FAQ</li><li>CONTACT US</li></ul>
</div>
<div class="f-divider abs" style="left:352px"></div>
<div class="f-col abs" style="left:383px;top:997px">
  <h4>CHIRPER FEED</h4>
  <p class="tweet">Nunc tempus felis vitae urna. Vivamus porttitor, g, purus nisi eleifend libero, a tempus<small>Posted 3 hours ago</small></p>
  <p class="tweet" style="margin-top:14px">Nunc tempus felis vitae urna. Vivamus porttitor, g, purus nisi eleifend libero, a tempus<small>Posted 3 hours ago</small></p>
</div>
<div class="f-divider abs" style="left:609px"></div>
<div class="f-col connect abs" style="left:652px;top:997px">
  <h4>GET CONNECTED</h4>
  <ul style="margin-left:2px"><li><i></i>Socialia</li><li><i></i>Chirper</li><li><i></i>Linkwork</li><li><i></i>RSS</li></ul>
</div>

<div class="footer-base abs"></div>
<div class="copyright abs">© 2013 Company Name.&nbsp; All right reserved.&nbsp; Term of Use</div>

</body>
</html>
```